Project Title:
Dental Implant Overdenture Flyer (Retirement Village Target)
Objective:
Create a clean, trustworthy, and reassuring flyer aimed at older adults (60–85 years old) who struggle with loose dentures. The goal is to educate them about implant-retained “clip-on” dentures and encourage them to book a consultation.
Tone & Feel:
Warm, caring, non-intimidating
Premium but not “salesy”
Medical but easy to understand
Focus on improving quality of life (confidence, eating, comfort)
Target Audience:
Retirees / pensioners
Existing denture wearers
People frustrated with loose or uncomfortable dentures
Key Message:
“You don’t have to live with loose dentures anymore.”
Design Style:
Clean, minimal, modern
Soft colours (blues, greens, warm neutrals)
Easy-to-read large font
High contrast for older eyes
Avoid clutter
Imagery Suggestions:
Smiling older adults (natural, not stocky/overly staged)
Before/after lifestyle (eating, laughing, socialising)
Simple diagram showing denture clipping onto implants
Avoid graphic surgical images
Layout Suggestions:
A5 or DL flyer
Clear sections with headings
Icons for benefits
Strong call-to-action at bottom
HEADLINE (big and bold)
Tired of Loose Dentures?
Discover Secure “Clip-On” Teeth
🔹 PROBLEM SECTION
Do your dentures:
Slip or move when eating?
Make it hard to chew certain foods?
Feel uncomfortable or loose?
Affect your confidence when speaking or smiling?
You’re not alone — and there is a better solution.
🔹 SOLUTION SECTION
Implant-Retained “Clip-On” Dentures
We can secure your denture using just 2 dental implants, allowing your teeth to:
✔ Stay firmly in place
✔ Improve your ability to eat
✔ Feel more comfortable
✔ Boost your confidence
🔹 SIMPLE EXPLANATION (very important)
Small titanium implants are gently placed in the jaw.
Your denture then clips securely onto them, stopping movement.
🔹 PRICE SECTION (highlight this clearly)
$12,000
Includes:
2 dental implants
A brand new custom overdenture
Does not include sedation or extractions (if needed)
🔹 SEDATION
Sedation is available for comfort.
If you hold a pensioner card, you may receive a significant Vantacor rebate, often resulting in minimal out-of-pocket costs for sedation.
🔹 TRUST / REASSURANCE
Experienced implant clinician
Gentle, patient-focused care
Modern technology and techniques
🔹 CALL TO ACTION (VERY IMPORTANT)
Book a Free Consultation
📞 Call: 08 9351 4276
🌐 Visit: www.bravonclinic.com.au
📍 Located near Tallowmere shopping centre
🔹 OPTIONAL TAGLINE
Eat Better. Feel Better. Smile with Confidence Again.
Please include some photos to illustrate what a clip on denture looks like with two implants.

```html
<!DOCTYPE html>
<html lang="en">
<head>
<meta charset="utf-8">
<title>Bravon Dental Clinic – Clip-On Dentures Flyer</title>
<link href="https://fonts.googleapis.com/css2?family=Poppins:ital,wght@0,300;0,400;0,500;0,600;0,700;1,400&display=swap" rel="stylesheet">
<style>
  :root {
    --teal: #1a9bb4;
    --teal-light: #3fd0c9;
    --teal-text: #1796b0;
    --ink: #111111;
    --body: #1d1d1d;
    --muted: #9aa3a6;
    --panel: #ececec;
    --band: #efefef;
    --page: #a9a9a9;
    --white: #ffffff;
  }
  * { margin: 0; padding: 0; box-sizing: border-box; }
  html, body { width: 1200px; height: 2400px; overflow: hidden; }
  body { background: var(--page); font-family: 'Poppins', sans-serif; color: var(--body); }

  .flyer {
    position: absolute; left: 100px; top: 490px;
    width: 1000px; height: 1420px;
    background: var(--white); overflow: hidden;
    box-shadow: 0 20px 40px rgba(0,0,0,.25);
  }
  .abs { position: absolute; }

  .hero-art { position: absolute; left: 0; top: 0; }

  .brand { left: 63px; top: 50px; display: flex; align-items: center; gap: 12px; }
  .brand-dot { width: 34px; height: 34px; border-radius: 50%; background: var(--teal); }
  .brand-name { font-weight: 500; font-size: 21px; color: var(--teal); letter-spacing: .5px; }

  .headline { left: 58px; top: 140px; font-size: 80px; line-height: 72px; color: var(--ink); font-weight: 400; letter-spacing: -1px; }
  .headline strong { font-weight: 700; }
  .subhead { left: 58px; top: 313px; font-size: 30px; color: var(--ink); }
  .subhead strong { font-weight: 700; }

  .section-title { font-weight: 600; font-size: 27px; color: var(--ink); }
  .section-title .accent { color: var(--teal-text); }

  .problem-title { left: 58px; top: 438px; }
  .problem-list { left: 58px; top: 482px; width: 470px; list-style: none; font-size: 21px; line-height: 28px; }
  .problem-list li { position: relative; padding-left: 26px; }
  .problem-list li::before { content: ""; position: absolute; left: 2px; top: 11px; width: 8px; height: 8px; border-radius: 50%; background: var(--teal); }
  .reassure { left: 58px; top: 664px; width: 420px; font-size: 24px; line-height: 27px; font-weight: 600; color: var(--teal-text); }

  .divider { left: 58px; top: 737px; width: 484px; border-top: 1.5px dashed #c9c9c9; }

  .solution-title { left: 58px; top: 764px; }
  .solution-text { left: 58px; top: 808px; width: 520px; font-size: 21px; line-height: 23px; }
  .benefit-list { left: 58px; top: 866px; list-style: none; font-size: 21px; line-height: 29px; }
  .benefit-list li { display: flex; align-items: center; gap: 10px; }
  .tick { width: 14px; height: 14px; flex: none; }

  .photo { top: 1008px; width: 213px; height: 105px; border-radius: 10px; background: linear-gradient(120deg, #6f5a45 0%, #b9a28a 45%, #e8dccd 70%, #8a7560 100%); }
  .photo-one { left: 58px; }
  .photo-two { left: 288px; }

  .how-title { left: 625px; top: 438px; font-size: 22px; font-weight: 600; color: var(--muted); letter-spacing: .5px; }
  .step { left: 625px; width: 313px; height: 103px; background: var(--panel); border-radius: 4px; display: flex; align-items: center; gap: 16px; padding: 0 14px; }
  .step-one { top: 473px; }
  .step-two { top: 585px; }
  .step-diagram { width: 100px; height: 68px; flex: none; border-radius: 4px; background: linear-gradient(160deg, #f7fbfd 0%, #cfe3ec 55%, #e9c2bd 100%); border: 1px solid #d5dde0; }
  .step-text { font-size: 16px; line-height: 17px; color: var(--body); }

  .price-box { left: 625px; top: 732px; width: 313px; height: 237px; border: 2px dashed var(--teal); border-radius: 14px; padding: 22px 30px; }
  .scissors { position: absolute; left: 140px; top: -14px; background: var(--white); padding: 0 4px; }
  .price { font-size: 56px; font-weight: 700; color: var(--teal-text); line-height: 62px; }
  .price-detail { margin-top: 16px; font-size: 17px; line-height: 19px; color: #555; }
  .price-detail strong { color: var(--ink); font-weight: 600; }

  .sedation-title { left: 625px; top: 1007px; font-size: 18px; font-weight: 700; color: var(--teal-text); }
  .sedation-text { left: 625px; top: 1036px; width: 320px; font-size: 14px; line-height: 16px; }

  .trust-band { left: 0; top: 1134px; width: 1000px; height: 117px; background: var(--band); }
  .trust-item { top: 1156px; display: flex; align-items: center; gap: 22px; font-size: 18px; line-height: 17px; }
  .trust-icon { width: 74px; height: 74px; flex: none; }
  .trust-one { left: 58px; }
  .trust-two { left: 352px; }
  .trust-three { left: 657px; }

  .cta-band { left: 0; top: 1251px; width: 1000px; height: 90px; background: var(--teal); }
  .cta-button { left: 55px; top: 1268px; width: 427px; height: 52px; background: var(--ink); border-radius: 10px; color: var(--white); font-size: 26px; display: flex; align-items: center; padding-left: 40px; }
  .phone { left: 555px; top: 1266px; display: flex; align-items: center; gap: 16px; color: var(--white); font-size: 42px; font-weight: 700; line-height: 44px; }
  .web-line { left: 555px; top: 1320px; color: var(--white); font-size: 12px; font-weight: 600; }

  .tagline { left: 0; top: 1362px; width: 1000px; text-align: center; font-style: italic; font-size: 23px; color: #666; }
</style>
</head>
<body>
<main class="flyer">

  <svg class="hero-art" width="1000" height="440" viewBox="0 0 1000 440">
    <defs>
      <linearGradient id="photoFade" x1="0" y1="0" x2="1" y2="0">
        <stop offset="0" stop-color="#ffffff"/>
        <stop offset=".45" stop-color="#e6ddd2"/>
        <stop offset="1" stop-color="#a99886"/>
      </linearGradient>
      <linearGradient id="waveTeal" x1="0" y1="0" x2="1" y2="0">
        <stop offset="0" stop-color="#3fd0c9"/>
        <stop offset="1" stop-color="#1790b0"/>
      </linearGradient>
    </defs>
    <rect x="480" y="0" width="520" height="360" fill="url(#photoFade)" role="img" aria-label="Photo of a smiling older man laughing"/>
    <path d="M0,362 C300,440 650,360 1000,150 L1000,245 C700,380 330,430 0,400 Z" fill="url(#waveTeal)"/>
    <path d="M0,400 C330,430 700,380 1000,245 L1000,440 L0,440 Z" fill="#ffffff"/>
  </svg>

  <div class="abs brand"><span class="brand-dot"></span><span class="brand-name">Bravon Dental Clinic</span></div>

  <h1 class="abs headline">Tired of <strong>Loose</strong><br><strong>Dentures?</strong></h1>
  <p class="abs subhead">Discover Secure <strong>“Clip-On”</strong> Teeth</p>

  <h2 class="abs section-title problem-title">Do your dentures</h2>
  <ul class="abs problem-list">
    <li>Slip or move when eating?</li>
    <li>Make it hard to chew certain foods?</li>
    <li>Make it hard to chew certain foods?</li>
    <li>Feel uncomfortable or loose?</li>
    <li>Affect your confidence when speaking or smiling?</li>
  </ul>
  <p class="abs reassure">You’re not alone and there is a better solution.</p>

  <div class="abs divider"></div>

  <h2 class="abs section-title solution-title">Implant-Retained <span class="accent">“Clip-On”</span> Dentures</h2>
  <p class="abs solution-text">We can secure your denture using just 2 dental implants, allowing your teeth to:</p>
  <ul class="abs benefit-list">
    <li><svg class="tick" viewBox="0 0 14 14"><circle cx="7" cy="7" r="7" fill="#1a9bb4"/><path d="M3.5,7.2 L6,9.5 L10.5,4.5" stroke="#fff" stroke-width="1.8" fill="none"/></svg>Stay firmly in place</li>
    <li><svg class="tick" viewBox="0 0 14 14"><circle cx="7" cy="7" r="7" fill="#1a9bb4"/><path d="M3.5,7.2 L6,9.5 L10.5,4.5" stroke="#fff" stroke-width="1.8" fill="none"/></svg>Improve your ability to eat</li>
    <li><svg class="tick" viewBox="0 0 14 14"><circle cx="7" cy="7" r="7" fill="#1a9bb4"/><path d="M3.5,7.2 L6,9.5 L10.5,4.5" stroke="#fff" stroke-width="1.8" fill="none"/></svg>Feel more comfortable</li>
    <li><svg class="tick" viewBox="0 0 14 14"><circle cx="7" cy="7" r="7" fill="#1a9bb4"/><path d="M3.5,7.2 L6,9.5 L10.5,4.5" stroke="#fff" stroke-width="1.8" fill="none"/></svg>Boost your confidence</li>
  </ul>

  <div class="abs photo photo-one" role="img" aria-label="Photo of a smiling older woman at home, hand on cheek"></div>
  <div class="abs photo photo-two" role="img" aria-label="Photo of the same older woman smiling confidently"></div>

  <h3 class="abs how-title">HOW IT WORKS</h3>
  <div class="abs step step-one">
    <div class="step-diagram" role="img" aria-label="Diagram of two implants placed in the lower jaw"></div>
    <p class="step-text">Small titanium implants are gently placed in the jaw.</p>
  </div>
  <div class="abs step step-two">
    <div class="step-diagram" role="img" aria-label="Diagram of a denture clipping onto two implants"></div>
    <p class="step-text">Your denture then clips securely onto them, stopping movement.</p>
  </div>

  <div class="abs price-box">
    <svg class="scissors" width="28" height="22" viewBox="0 0 28 22"><circle cx="6" cy="5" r="3.5" fill="none" stroke="#111" stroke-width="2"/><circle cx="6" cy="17" r="3.5" fill="none" stroke="#111" stroke-width="2"/><path d="M9,7 L25,17 M9,15 L25,5" stroke="#111" stroke-width="2"/></svg>
    <p class="price">$12,000</p>
    <p class="price-detail">INCLUDES:<br><strong>2 dental implants<br>A brand new custom overdenture</strong><br>Does not include sedation or extractions (if needed)</p>
  </div>

  <p class="abs sedation-title">Sedation is available for comfort.</p>
  <p class="abs sedation-text">If you hold a pensioner card, you may receive a significant Vantacor rebate, often resulting in minimal out-of-pocket costs for sedation.</p>

  <div class="abs trust-band"></div>
  <div class="abs trust-item trust-one">
    <svg class="trust-icon" viewBox="0 0 74 74"><circle cx="37" cy="37" r="35" fill="none" stroke="#1a9bb4" stroke-width="1.5"/><path d="M24,26 C24,19 31,18 37,22 C43,18 50,19 50,26 C50,34 46,38 45,48 C44,54 40,54 39,46 L37,40 L35,46 C34,54 30,54 29,48 C28,38 24,34 24,26 Z" fill="none" stroke="#333" stroke-width="2"/><path d="M44,34 h8 M48,30 v8" stroke="#333" stroke-width="2"/></svg>
    <span>Experienced<br>implant clinician</span>
  </div>
  <div class="abs trust-item trust-two">
    <svg class="trust-icon" viewBox="0 0 74 74"><circle cx="37" cy="37" r="35" fill="none" stroke="#1a9bb4" stroke-width="1.5"/><path d="M30,28 C30,23 34,22 37,25 C40,22 44,23 44,28 C44,33 42,36 41,42 L37,38 L33,42 C32,36 30,33 30,28 Z" fill="none" stroke="#333" stroke-width="2"/><path d="M20,30 L22,46 L30,54 M54,30 L52,46 L44,54" fill="none" stroke="#333" stroke-width="2"/></svg>
    <span>Gentle, patient-<br>focused care</span>
  </div>
  <div class="abs trust-item trust-three">
    <svg class="trust-icon" viewBox="0 0 74 74"><circle cx="37" cy="37" r="35" fill="none" stroke="#1a9bb4" stroke-width="1.5"/><rect x="21" y="22" width="32" height="24" rx="2" fill="none" stroke="#333" stroke-width="2"/><path d="M37,46 v6 M29,53 h16" stroke="#333" stroke-width="2"/><path d="M31,29 C31,26 34,26 37,28 C40,26 43,26 43,29 C43,33 41,35 40,40 L37,37 L34,40 C33,35 31,33 31,29 Z" fill="none" stroke="#333" stroke-width="1.6"/></svg>
    <span>Modern technology<br>and techniques</span>
  </div>

  <div class="abs cta-band"></div>
  <div class="abs cta-button">Book a Free Consultation</div>
  <div class="abs phone">
    <svg width="34" height="34" viewBox="0 0 34 34"><circle cx="17" cy="17" r="16" fill="#3fd0c9"/><path d="M11,13 C11,11 13,10 17,10 C21,10 23,11 23,13 L21,14 L20,12.5 C18,12 16,12 14,12.5 L13,14 Z M12,23 L13,17 L21,17 L22,23 Z" fill="#fff"/></svg>
    <span>08 9351 4276</span>
  </div>
  <p class="abs web-line">www.bravonclinic.com.au &nbsp;|&nbsp; near Tallowmere shopping centre</p>

  <p class="abs tagline">Eat Better. Feel Better. Smile with Confidence Again.</p>
</main>
</body>
</html>
```